"Amberlane Vantage Harbor": unique end to end Chinese marketing and ecommerce solutions*

I would like to create a company website for my trademark: "Amberlane Vantage Harbor". We are based in Iceland. We are the only company in the market offering end-to-end Chinese digital marketing and eCommerce solutions. We help companies grow their brands and sales towards Chinese - whether tourism, export of products or services.
I include the logo that we have come up with in terms of colours and fonts.
The font is Trajan - I would like to use normal letters (capital and lowercase) for text.
Front page: Picture with colour filter. Logo in white. Text line underneath.
I am inspired by this website:
https://www.brindlecove.example/
I like these short videos for landing page:
https://www.pixelorchard.example/video/clip-48213907-misty-ridge-scenery
https://www.pixelorchard.example/video/clip-7390451128-4k-aerial-video-ridge-scenery
https://www.pixelorchard.example/video/clip-6620984315-ridge-scenery
Icelandic businesses looking for business opportunities in China or to attract Chinese tourists.
Digital Marketing

```html
<!DOCTYPE html>
<html lang="en">
<head>
<meta charset="utf-8">
<title>Amberlane Vantage Harbor</title>
<link rel="stylesheet" href="https://fonts.googleapis.com/css2?family=Cinzel:wght@400;600;700&family=Hind:wght@400;500&family=Open+Sans:wght@400&display=swap">
<style>
:root{
  --blue:#1b57a6;
  --gold:#b38c4b;
  --gold-light:#c29b5a;
  --ink:#1d1d1d;
  --cream:#fdf6ee;
  --navy:#1c2a3c;
  --white:#ffffff;
  --line:#3b5c8c;
}
*{box-sizing:border-box;margin:0;padding:0}
html,body{width:1200px;height:4829px;overflow:hidden;background:var(--white)}
body{position:relative;font-family:"Hind",sans-serif;color:var(--ink)}
a{text-decoration:none}
.abs{position:absolute}

/* hero */
.hero{left:0;top:0;width:1200px;height:632px;background:linear-gradient(180deg,#55646a 0%,#3e4a44 35%,#4c4a2c 65%,#2f2a18 100%)}
.brand{left:60px;top:26px;width:125px;text-align:center;color:var(--white);font-family:"Cinzel",serif;font-size:11px;line-height:13px;letter-spacing:.3px}
.brand .mark{display:block;width:26px;height:26px;border-radius:50%;border:2px solid var(--white);margin:0 auto 6px}
.menu{left:1072px;top:36px;width:56px;height:34px}
.menu span{display:block;height:4px;background:var(--white);margin-bottom:11px;border-radius:1px}
.hero-title{left:0;top:162px;width:1200px;text-align:center;color:var(--white);font-family:"Cinzel",serif;font-weight:700;font-size:74px;line-height:84px;letter-spacing:1px}
.hero-lead{left:0;top:344px;width:1200px;text-align:center;color:var(--white);font-size:27px;line-height:39px}
.btn{display:flex;align-items:center;justify-content:center;background:var(--gold);color:var(--white);font-family:"Cinzel",serif;font-size:15px;letter-spacing:.5px}
.hero-cta{left:523px;top:443px;width:154px;height:41px}

/* problem */
.problem-title{left:232px;top:730px;font-family:"Cinzel",serif;font-weight:700;font-size:40px;line-height:49px;color:var(--blue)}
.problem-title span{color:var(--gold)}
.about-btn{left:239px;top:917px;width:133px;height:36px;font-size:13px}
.problem-text{left:600px;top:736px;width:500px;font-family:"Open Sans",sans-serif;font-size:23px;line-height:28px;color:#111}
.problem-text p+p{margin-top:28px}

/* clients */
.clients{left:0;top:1041px;width:1200px;height:310px;background:var(--cream)}
.clients-title{left:0;top:1086px;width:1200px;text-align:center;font-family:"Cinzel",serif;font-weight:700;font-size:26px;color:#111}
.arrow-dot{width:34px;height:34px;border-radius:50%;background:#c9c4bd}
.client{width:146px;height:57px;background:var(--white);border:1px solid #eee6dc;display:flex;align-items:center;justify-content:center;font-weight:500;font-size:15px;color:var(--blue);text-align:center;line-height:16px}
.testimonial-btn{left:514px;top:1264px;width:172px;height:37px;font-size:14px}

/* services */
.photo{width:600px;height:401px}
.svc h3{font-family:"Cinzel",serif;font-weight:700;font-size:60px;line-height:62px;color:var(--blue)}
.svc p{font-size:17px;line-height:26px;color:#111;margin-top:30px;width:290px}
.more{display:flex;align-items:center;justify-content:center;gap:8px;width:140px;height:38px;border:2px solid var(--gold-light);color:var(--gold);font-family:"Cinzel",serif;font-size:13px;margin-top:34px;background:var(--white)}

/* contact */
.field{left:195px;width:379px;border-bottom:2px solid var(--line);background:#eef0f4;font-size:15px;color:#555;padding:8px 16px}
.send{left:195px;top:4389px;width:167px;height:38px;font-size:15px}
.contact-kicker{left:651px;top:4118px;font-family:"Cinzel",serif;font-weight:700;font-size:24px;color:var(--blue)}
.contact-head{left:651px;top:4162px;font-family:"Cinzel",serif;font-weight:700;font-size:28px;line-height:35px;color:#111}
.contact-call{left:651px;top:4304px;font-size:17px;color:var(--blue)}
.contact-phone{left:651px;top:4340px;font-family:"Cinzel",serif;font-weight:600;font-size:30px;color:#111}

/* footer */
.footer{left:0;top:4515px;width:1200px;height:314px;background:var(--navy)}
.footer-brand{left:220px;top:4560px;width:280px;text-align:center;color:var(--white);font-family:"Cinzel",serif;font-size:15px;line-height:20px}
.footer-brand .mark{display:block;width:40px;height:40px;border-radius:50%;border:2px solid var(--white);margin:0 auto 10px}
.footer-about{left:240px;top:4650px;width:240px;text-align:center;color:var(--gold-light);font-size:15px;line-height:24px}
.footer-col h4{font-family:"Cinzel",serif;font-weight:600;font-size:16px;color:var(--white);margin-bottom:14px}
.footer-col li{list-style:none;font-size:14px;line-height:25px;color:var(--gold-light)}
.footer-rule{left:0;top:4763px;width:1200px;height:1px;background:#34445a}
.footer-legal{top:4792px;font-size:11px;color:var(--gold-light)}
</style>
</head>
<body>

<header class="abs hero" role="img" aria-label="Misty mountain ridge with an ancient wall at dusk, tinted with a dark colour filter"></header>
<div class="abs brand"><span class="mark"></span>Amberlane Vantage Harbor</div>
<div class="abs menu"><span></span><span></span><span></span></div>
<h1 class="abs hero-title">GROW YOUR BRAND<br>AND SALES IN CHINA.</h1>
<p class="abs hero-lead">We help companies and businesses in Iceland<br>expand their presence in China</p>
<a class="abs btn hero-cta">Get In Touch</a>

<section>
  <h2 class="abs problem-title">REAL PROBLEM<br><span>REAL RESULT</span></h2>
  <a class="abs btn about-btn">About Us</a>
  <div class="abs problem-text">
    <p>We provide marketing and consulting services to startups, small businesses and large businesses looking to succeed in China. We work with you, not for you. Although we have great resources.</p>
    <p>We are headquartered in Iceland in order to best serve you.</p>
  </div>
</section>

<section class="abs clients"></section>
<h2 class="abs clients-title">OUR TRUSTED CLIENTS IN ICELAND</h2>
<div class="abs arrow-dot" style="left:120px;top:1173px"><svg width="34" height="34" viewBox="0 0 34 34"><path d="M20 10 L13 17 L20 24" stroke="#fff" stroke-width="2.5" fill="none"/></svg></div>
<div class="abs client" style="left:197px;top:1162px">Northpine Academy</div>
<div class="abs client" style="left:362px;top:1162px">Larkfield Travel</div>
<div class="abs client" style="left:527px;top:1162px">Summit Grove Games</div>
<div class="abs client" style="left:692px;top:1162px">Ravenmoor Motors</div>
<div class="abs client" style="left:857px;top:1162px">Tallybrook Web</div>
<div class="abs arrow-dot" style="left:1046px;top:1173px"><svg width="34" height="34" viewBox="0 0 34 34"><path d="M14 10 L21 17 L14 24" stroke="#fff" stroke-width="2.5" fill="none"/></svg></div>
<a class="abs btn testimonial-btn">Read Testimonial</a>

<section class="svc">
  <div class="abs photo" style="left:600px;top:1414px;background:linear-gradient(135deg,#c7d3dc,#7f93a8 60%,#3b4c66)" role="img" aria-label="Woman in a shopping mall looking at her phone"></div>
  <div class="abs" style="left:161px;top:1473px">
    <h3>MARKET<br>RESEARCH</h3>
    <p>We identify and analyze business opportunities in China.</p>
    <a class="more">Read More <svg width="18" height="10" viewBox="0 0 18 10"><path d="M0 5 H16 M12 1 L16 5 L12 9" stroke="#b38c4b" stroke-width="1.6" fill="none"/></svg></a>
  </div>
</section>

<section class="svc">
  <div class="abs photo" style="left:0;top:1948px;background:linear-gradient(180deg,#a9c1cc,#6f8a8e 50%,#3f5248)" role="img" aria-label="Hiker on stone steps of an ancient wall climbing a misty mountain"></div>
  <div class="abs" style="left:718px;top:2023px">
    <h3>TOURISM</h3>
    <p>Lorem ipsum dolor sit amet, consetetur sadipscing elitr, sed diam nonumy eirmod tempor</p>
    <a class="more">Read More <svg width="18" height="10" viewBox="0 0 18 10"><path d="M0 5 H16 M12 1 L16 5 L12 9" stroke="#b38c4b" stroke-width="1.6" fill="none"/></svg></a>
  </div>
</section>

<section class="svc">
  <div class="abs photo" style="left:600px;top:2483px;background:linear-gradient(180deg,#c9d2c4,#a08a6c 45%,#6b5a52)" role="img" aria-label="Busy pedestrian shopping street with shop signs in a Chinese city"></div>
  <div class="abs" style="left:161px;top:2543px">
    <h3>DIGITAL<br>MARKETING</h3>
    <p>Lorem ipsum dolor sit amet, consetetur sadipscing elitr, sed</p>
    <a class="more">Read More <svg width="18" height="10" viewBox="0 0 18 10"><path d="M0 5 H16 M12 1 L16 5 L12 9" stroke="#b38c4b" stroke-width="1.6" fill="none"/></svg></a>
  </div>
</section>

<section class="svc">
  <div class="abs photo" style="left:0;top:3017px;background:linear-gradient(135deg,#2c3a4e,#8a5a52 45%,#cfc5b4)" role="img" aria-label="Person browsing an online shopping site on a laptop"></div>
  <div class="abs" style="left:718px;top:3055px">
    <h3>ECOMMERCE<br>SOLUTION</h3>
    <p>Lorem ipsum dolor sit amet, consetetur sadipscing elitr, sed diam nonumy eirmod tempor</p>
    <a class="more">Read More <svg width="18" height="10" viewBox="0 0 18 10"><path d="M0 5 H16 M12 1 L16 5 L12 9" stroke="#b38c4b" stroke-width="1.6" fill="none"/></svg></a>
  </div>
</section>

<section class="svc">
  <div class="abs photo" style="left:600px;top:3551px;background:linear-gradient(135deg,#6f9cc4,#a8c3db 50%,#e1e8ef)" role="img" aria-label="Hands typing on a laptop showing a mobile payment screen"></div>
  <div class="abs" style="left:161px;top:3644px">
    <h3>PAYMENTS</h3>
    <p>Lorem ipsum dolor sit amet, consetetur sadipscing elitr, sed</p>
    <a class="more">Read More <svg width="18" height="10" viewBox="0 0 18 10"><path d="M0 5 H16 M12 1 L16 5 L12 9" stroke="#b38c4b" stroke-width="1.6" fill="none"/></svg></a>
  </div>
</section>

<section>
  <div class="abs field" style="top:4119px;height:36px">Email Address</div>
  <div class="abs field" style="top:4184px;height:36px">Subject</div>
  <div class="abs field" style="top:4249px;height:114px">Your Message</div>
  <a class="abs btn send">Send Message</a>
  <div class="abs contact-kicker">Get In Touch</div>
  <div class="abs contact-head">DON'T HESITATE TO<br>CONTACT US FOR<br>FURTHER</div>
  <div class="abs contact-call">Call us for immediate consultation</div>
  <div class="abs contact-phone">+100 555 0199</div>
</section>

<footer class="abs footer"></footer>
<div class="abs footer-brand"><span class="mark"></span>Amberlane Vantage Harbor</div>
<div class="abs footer-about">Lorem ipsum dolor sit amet, consetetur sadipscing elitr, sed diam nonumy eirmod.</div>
<div class="abs footer-col" style="left:581px;top:4560px">
  <h4>Our Services</h4>
  <ul><li>Market Research</li><li>Tourism</li><li>Digital Marketing</li><li>Ecommerce Solution</li></ul>
</div>
<div class="abs footer-col" style="left:831px;top:4560px">
  <h4>Get Connected</h4>
  <ul><li>ChatLoop</li><li>ClipStream</li><li>ProLink Circle</li><li>FriendSquare</li></ul>
</div>
<div class="abs footer-rule"></div>
<div class="abs footer-legal" style="left:258px">Terms &amp; Conditions</div>
<div class="abs footer-legal" style="left:388px">Privacy Policy</div>
<div class="abs footer-legal" style="left:641px">© 2020 Amberlane Vantage Harbor. All rights reserved.</div>

</body>
</html>
```